Build Your Own Shake Menu Design

Menu Design
- will be printed on countertop acrylic menu stands that are a foot by a foot

Files:
- document attached for the menu contents
*file name: SHAKEMENU
- sample menu images (these are giant acrylic menu boards that are in my shop)
*file name: newest shave ice menu, newest spi rolls menu (JPG)
-picture of the shop where the menus will be placed
*file name: shop (PNG)

```html
<!DOCTYPE html>
<html lang="en">
<head>
<meta charset="utf-8">
<title>Create Your Own Shake Menu</title>
<link href="https://fonts.googleapis.com/css2?family=Lilita+One&family=Lobster&family=Poppins:wght@500;600;700&family=Kaushan+Script&family=Fredericka+the+Great&family=Alfa+Slab+One&family=Gochi+Hand&family=Abril+Fatface&display=swap" rel="stylesheet">
<style>
:root{
  --bg:#dcdcdc;
  --paper:#f4f4f4;
  --red:#c4112b;
  --deep-red:#9e0b1f;
  --pink:#f0607f;
  --yellow:#f4c21a;
  --gold:#e3a41b;
  --navy:#1c2140;
  --ink:#2a2a2a;
  --grey:#6d6d6d;
  --blue:#2f3bd6;
  --magenta:#e0319a;
  --violet:#7b3fd0;
  --orange:#f08a2c;
}
*{box-sizing:border-box;margin:0;padding:0}
html,body{width:1200px;height:900px;overflow:hidden}
body{background:var(--bg);font-family:"Poppins",sans-serif;position:relative}
.panel{position:absolute;top:30px;width:380px;height:840px;background:var(--paper);overflow:hidden;box-shadow:0 4px 14px rgba(0,0,0,.18)}
.panel--base{left:20px}
.panel--toppings{left:410px}
.panel--drinks{left:800px}
.abs{position:absolute}
.photo{position:absolute}

/* left panel */
.corner-shape{position:absolute;top:0;left:0}
.create-tag{left:150px;top:22px;background:var(--navy);color:#fff;font-family:"Lilita One",sans-serif;font-size:30px;padding:0 14px;border-radius:20px;border:3px solid var(--yellow)}
.your-own{left:82px;top:66px;font-family:"Lilita One",sans-serif;font-size:22px;color:var(--navy);letter-spacing:2px}
.shake-word{left:95px;top:90px;font-family:"Lobster",cursive;font-size:46px;color:var(--red)}
.menu-word{left:40px;top:150px;font-family:"Lobster",cursive;font-size:110px;color:var(--yellow);line-height:1}
.section-bar{position:absolute;height:36px;background:linear-gradient(90deg,rgba(0,0,0,0),#cfcfcf 20%,#cfcfcf 80%,rgba(0,0,0,0));font-family:"Lilita One",sans-serif;font-size:25px;color:var(--ink);text-align:center;line-height:36px;white-space:nowrap}
.standard{left:0;width:380px;top:335px;text-align:center;font-family:"Fredericka the Great",serif;font-size:26px;color:var(--grey)}
.flavour-line{left:0;width:380px;text-align:center;font-family:"Abril Fatface",serif;color:var(--red);white-space:nowrap}
.flavour-line .dot{display:inline-block;width:22px;height:9px;background:var(--yellow);border-radius:50%;transform:rotate(-25deg);margin:0 8px;vertical-align:middle}
.badge{position:absolute;width:70px;height:70px;border-radius:50%;background:radial-gradient(circle,var(--red) 55%,#fff 57%,#fff 66%,#bbb 68%);color:#fff;font-family:"Alfa Slab One",serif;font-size:22px;display:flex;flex-direction:column;align-items:center;justify-content:center;line-height:1}
.badge small{font-family:"Poppins",sans-serif;font-size:8px}
.price{position:absolute;width:148px;height:36px}
.price .pill{position:absolute;left:0;top:2px;width:54px;height:32px;background:#fff;border-radius:16px;box-shadow:0 2px 4px rgba(0,0,0,.25);font-family:"Alfa Slab One",serif;font-size:15px;color:var(--red);display:flex;align-items:center;justify-content:center}
.price .bar{position:absolute;left:40px;top:0;width:108px;height:36px;background:#fff;border-right:8px solid var(--red);border-top:4px solid var(--red);transform:skewX(-10deg);box-shadow:0 2px 4px rgba(0,0,0,.2)}
.price .label{position:absolute;left:60px;top:4px;width:80px;font-size:10px;line-height:13px;color:var(--grey);font-style:italic;text-align:center;white-space:nowrap}

/* middle panel */
.free-ring{left:12px;top:8px;width:140px;height:140px;border-radius:50%;border:12px solid var(--red);border-right-color:transparent;transform:rotate(-30deg)}
.free-word{left:30px;top:28px;font-family:"Lobster",cursive;font-size:56px;color:var(--red)}
.whip{left:175px;top:8px;font-size:12px;font-weight:700;color:var(--ink)}
.cream{left:170px;top:20px;font-family:"Lilita One",sans-serif;font-size:32px;color:var(--gold);line-height:1}
.amp{left:232px;top:52px;font-size:10px;font-weight:700}
.cherry{left:170px;top:60px;font-family:"Lilita One",sans-serif;font-size:32px;color:var(--red);line-height:1}
.to-every{left:212px;top:90px;font-size:10px;font-weight:700}
.milkshake{left:118px;top:102px;font-family:"Lobster",cursive;font-size:48px;color:var(--red)}
.choose-band{left:8px;top:195px;width:364px;height:48px;background:var(--red);color:#fff;text-align:center;font-family:"Kaushan Script",cursive;font-size:16px;line-height:24px;padding-top:2px}
.choose-band span{display:block;font-size:12px;line-height:16px;color:var(--yellow)}
.topping{position:absolute;left:12px;width:356px;height:24px;background:linear-gradient(90deg,rgba(255,255,255,0),#fff 12%,#fff 88%,rgba(255,255,255,0));border-bottom:3px solid var(--red);font-size:11.5px;font-weight:500;color:var(--ink);text-align:center;line-height:22px;white-space:nowrap;overflow:hidden;box-shadow:0 3px 4px rgba(196,17,43,.18)}

/* right panel */
.drinks-title{left:70px;top:45px;width:240px}
.drink{position:absolute;height:34px}
.drink .pill{position:absolute;left:0;top:2px;width:54px;height:30px;background:#fff;border-radius:15px;box-shadow:0 2px 4px rgba(0,0,0,.25);font-family:"Alfa Slab One",serif;font-size:14px;color:var(--red);display:flex;align-items:center;justify-content:center}
.drink .bar{position:absolute;left:40px;top:0;height:34px;background:#fff;border-right:8px solid var(--red);border-top:4px solid var(--red);transform:skewX(-10deg);box-shadow:0 2px 4px rgba(0,0,0,.2)}
.drink .label{position:absolute;left:66px;top:9px;font-size:11px;font-style:italic;font-weight:600;color:var(--grey);white-space:nowrap}
.spoons-title{left:20px;top:342px;width:340px}
.spoon-row{position:absolute;left:18px;width:345px;display:flex;font-family:"Gochi Hand",cursive;font-size:34px;line-height:1}
.spoon-row .from{width:122px}
.spoon-row .to{width:60px;color:var(--ink);font-size:26px;padding-top:6px}
.spoon-badge{left:128px;top:588px;width:112px;height:112px;border-radius:50%;background:radial-gradient(circle,var(--red) 46%,#fff 48%,#fff 70%,#c9c9c9 72%);display:flex;flex-direction:column;align-items:center;justify-content:center;color:#fff;font-family:"Alfa Slab One",serif;font-size:30px;line-height:1}
.spoon-badge small{font-family:"Poppins",sans-serif;font-size:9px}
.spoon-badge .ring-text{position:absolute;top:0;left:0}
</style>
</head>
<body>

<section class="panel panel--base">
  <svg class="corner-shape" width="380" height="130" viewBox="0 0 380 130">
    <path d="M0 0H210C170 10 120 30 70 70C40 95 20 110 0 120Z" fill="var(--yellow)"/>
    <path d="M120 0H230C200 10 170 20 150 30C140 20 130 10 120 0Z" fill="var(--navy)"/>
    <circle cx="270" cy="22" r="7" fill="none" stroke="var(--red)" stroke-width="2"/>
    <circle cx="272" cy="50" r="6" fill="var(--red)"/>
    <circle cx="284" cy="64" r="4" fill="var(--gold)"/>
  </svg>
  <div class="abs create-tag">Create</div>
  <div class="abs your-own">Your Own</div>
  <div class="abs shake-word">Shake</div>
  <div class="abs menu-word">menu</div>

  <div class="section-bar" style="left:40px;top:290px;width:300px">Choose Your Base</div>
  <div class="abs standard">Standard Base</div>
  <div class="abs flavour-line" style="top:372px;font-size:32px">Vanilla<span class="dot"></span>Chocolate</div>

  <div class="section-bar" style="left:10px;top:430px;width:260px">Specialty Bases</div>
  <div class="badge" style="left:272px;top:405px">.50<small>Cent</small></div>
  <div class="abs flavour-line" style="top:478px;font-size:30px">Mint<span class="dot"></span>Strawberry</div>
  <div class="abs flavour-line" style="top:518px;font-size:30px">Espresso<span class="dot"></span>Cheesecake</div>

  <div class="price" style="left:14px;top:574px"><div class="bar"></div><div class="pill">$5.75</div><div class="label">15 Ounce<br>Regular</div></div>
  <div class="price" style="left:186px;top:574px"><div class="bar"></div><div class="pill">$6.25</div><div class="label">15 Ounce<br>Specialty Base</div></div>
  <div class="price" style="left:14px;top:622px"><div class="bar"></div><div class="pill">$5.99</div><div class="label">18 Ounce<br>Large</div></div>
  <div class="price" style="left:186px;top:622px"><div class="bar"></div><div class="pill">$6.49</div><div class="label">18 Ounce<br>Specialty Base</div></div>

  <div class="photo" role="img" aria-label="Rolled ice cream cups with strawberries over a pink milk splash" style="left:0;top:680px;width:380px;height:160px;background:linear-gradient(180deg,rgba(240,96,127,0) 0%,#f6a3b4 35%,var(--pink) 100%)"></div>
</section>

<section class="panel panel--toppings">
  <div class="abs free-ring"></div>
  <div class="abs free-word">free</div>
  <div class="abs whip">Whip</div>
  <div class="abs cream">CREAM</div>
  <div class="abs amp">&amp; A</div>
  <div class="abs cherry">CHERRY</div>
  <div class="abs to-every">to Every</div>
  <div class="photo" role="img" aria-label="Whipped cream milkshakes in tall glasses" style="left:20px;top:100px;width:100px;height:92px;background:radial-gradient(circle,#9a5a3a,#e8c9a8 70%,rgba(0,0,0,0))"></div>
  <div class="abs milkshake">Milkshake</div>

  <div class="abs choose-band">Choose Up To 2 Items For Your Shake<span>Additions Choice</span></div>

  <div class="topping" style="top:252px">Cookie Dough-Peanut Butter Cup-Peanut Crunch Bar</div>
  <div class="topping" style="top:286px">Mint Squares-Toffee-Cookie Chips-Graham Crackers</div>
  <div class="topping" style="top:320px">Cookie Crumble-Chocolate Chips-White Chocolate Chips</div>
  <div class="topping" style="top:354px">Rainbow Sprinkles-Cupcake Bites-Candy Buttons</div>
  <div class="topping" style="top:388px">Nuts-Almonds-Strawberries-Banana-Cherries</div>
  <div class="topping" style="top:422px">Corn Crunch Cereal-Cinnamon Squares</div>
  <div class="topping" style="top:456px">Fruity Flakes-Cocoa Flakes</div>
  <div class="topping" style="top:490px">Peanut Butter Drizzle-Chocolate Drizzle</div>
  <div class="topping" style="top:524px">Strawberry Drizzle-Raspberry Drizzle</div>
  <div class="topping" style="top:558px">Marshmallow Drizzle</div>

  <div class="photo" role="img" aria-label="Cups of rolled ice cream with colourful toppings over a pink splash" style="left:0;top:610px;width:380px;height:230px;background:linear-gradient(180deg,rgba(240,96,127,0) 0%,#f3c9a0 30%,#f6a3b4 60%,var(--pink) 100%)"></div>
</section>

<section class="panel panel--drinks">
  <svg class="corner-shape" width="380" height="80" viewBox="0 0 380 80">
    <path d="M170 0H380V60C330 40 280 30 230 20C205 14 185 8 170 0Z" fill="var(--yellow)"/>
    <path d="M170 0H270C250 10 230 20 215 30C195 20 180 10 170 0Z" fill="var(--navy)"/>
  </svg>
  <div class="section-bar drinks-title">Drinks</div>

  <div class="drink" style="left:14px;top:90px"><div class="bar" style="width:118px"></div><div class="pill">$1.00</div><div class="label">Water</div></div>
  <div class="drink" style="left:14px;top:138px"><div class="bar" style="width:118px"></div><div class="pill">$1.99</div><div class="label">Cola</div></div>
  <div class="drink" style="left:14px;top:186px"><div class="bar" style="width:118px"></div><div class="pill">$1.99</div><div class="label">Lemon-Lime</div></div>
  <div class="drink" style="left:174px;top:186px"><div class="bar" style="width:150px"></div><div class="pill">$1.99</div><div class="label" style="left:92px">Tea</div></div>
  <div class="drink" style="left:14px;top:236px"><div class="bar" style="width:236px"></div><div class="pill">$1.99</div><div class="label">Sport Drink Fruit Punch</div></div>
  <div class="photo" role="img" aria-label="Bottled water, sodas and sport drinks" style="left:180px;top:82px;width:150px;height:92px;background:linear-gradient(90deg,#c8dff0,#c4112b 40%,#3a9a4a 60%,#f08a2c 80%,#c8dff0)"></div>

  <div class="section-bar spoons-title">Color Changing Spoons</div>
  <div class="spoon-row" style="top:398px"><span class="from" style="color:var(--blue)">White</span><span class="to">to</span><span style="color:var(--blue)">Blue</span></div>
  <div class="spoon-row" style="top:442px"><span class="from" style="color:var(--magenta)">Pink</span><span class="to">to</span><span style="color:var(--violet)">Purple</span></div>
  <div class="spoon-row" style="top:486px"><span class="from" style="color:var(--blue)">White</span><span class="to">to</span><span style="color:var(--orange)">Confetti</span></div>

  <div class="photo" role="img" aria-label="Fan of colour changing spoons" style="left:110px;top:534px;width:150px;height:54px;background:linear-gradient(90deg,#3b4be0,#7b3fd0,#e0319a,#f4c21a,#f6e7c0)"></div>
  <div class="abs spoon-badge">
    <svg class="ring-text" width="112" height="112" viewBox="0 0 112 112">
      <defs><path id="spoonRing" d="M56 56m-44 0a44 44 0 1 1 88 0a44 44 0 1 1-88 0"/></defs>
      <text font-family="Poppins, sans-serif" font-size="8" font-weight="600" fill="var(--ink)"><textPath href="#spoonRing" startOffset="2%">COLOR CHANGING SPOONS IN 3 COLORS</textPath></text>
    </svg>
    .50<small>Cent</small>
  </div>

  <div class="photo" role="img" aria-label="Bottles and cans of soda, tea and water in a water splash" style="left:0;top:650px;width:380px;height:190px;background:linear-gradient(180deg,rgba(200,223,240,0) 0%,#c8dff0 35%,#8a1c24 70%,#3a3a3a 100%)"></div>
</section>

</body>
</html>
```